Korvel Reefworks business card

We sell live saltwater fish and live corals
Korvel Reefworks
7 Halden Ct
Sewell, NJ. 08080
(856) 319-7264
Contact Information for Business Card
Korvel Reefworks
7 Halden Ct
Sewell, NJ. 08080
(856) 319-7264
Colors
Designer to choose colors to be used in the design.

```html
<!DOCTYPE html>
<html lang="en">
<head>
<meta charset="utf-8">
<title>Korvel Reefworks business card</title>
<link rel="stylesheet" href="https://fonts.googleapis.com/css2?family=Poppins:wght@400&family=Roboto:ital,wght@0,700;1,400;1,700&display=swap">
<style>
  :root {
    --stage: #ecebe8;
    --card-blue: #283d96;
    --white: #ffffff;
    --cyan: #2fc3ea;
    --outline: #e8eef5;
    --fish: #f2582a;
  }
  * { margin: 0; padding: 0; box-sizing: border-box; }
  html, body { width: 900px; height: 1200px; overflow: hidden; }
  body { background: var(--stage); position: relative; }

  .card {
    position: absolute;
    left: 87px;
    width: 735px;
    height: 428px;
    background: var(--card-blue);
    overflow: hidden;
  }
  .card--rounded { top: 137px; border-radius: 20px; }
  .card--square { top: 633px; }

  .brand-name {
    position: absolute;
    left: 28px;
    top: 30px;
    font-family: "Roboto", sans-serif;
    font-weight: 700;
    font-size: 56px;
    letter-spacing: -1px;
    line-height: 1;
    color: var(--white);
  }
  .tagline {
    position: absolute;
    left: 31px;
    top: 100px;
    font-family: "Roboto", sans-serif;
    font-style: italic;
    font-weight: 400;
    font-size: 19px;
    color: var(--white);
  }
  .tagline strong { font-weight: 700; }

  .contact-line {
    position: absolute;
    left: 27px;
    display: flex;
    align-items: center;
    gap: 9px;
    font-family: "Poppins", sans-serif;
    font-size: 21px;
    color: var(--white);
  }
  .contact-line--phone { top: 157px; }
  .contact-line--address { top: 201px; }
  .contact-icon { width: 32px; height: 32px; flex: none; }

  .reef-scene { position: absolute; left: 0; top: 0; width: 735px; height: 428px; }
</style>
</head>
<body>

<section class="card card--rounded">
  <svg class="reef-scene" viewBox="0 0 735 428" role="img" aria-label="Photograph of a coral reef aquarium with rocks, pink and purple corals, and an orange cartoon fish">
    <defs>
      <linearGradient id="reef-tones-a" x1="0" y1="0" x2="1" y2="0.3">
        <stop offset="0" stop-color="#4b4a5c"/>
        <stop offset="0.4" stop-color="#7d6e86"/>
        <stop offset="0.7" stop-color="#8d6fa8"/>
        <stop offset="0.85" stop-color="#c86a72"/>
        <stop offset="1" stop-color="#9fae4c"/>
      </linearGradient>
    </defs>
    <path fill="url(#reef-tones-a)" stroke="var(--outline)" stroke-width="3" d="M0,428 V352 C20,340 40,352 55,345 C70,338 85,290 95,280 C110,268 120,290 118,310 C116,330 125,345 140,340 C155,335 170,330 185,330 C195,300 190,265 205,258 C225,250 235,275 225,290 C215,305 245,300 250,310 C255,320 265,300 275,290 C285,275 300,265 315,280 C325,295 320,330 335,345 C345,340 350,320 360,300 C370,285 385,290 385,310 C385,330 390,345 405,340 C415,330 430,285 445,270 C460,255 470,270 468,300 C466,330 470,345 480,345 C490,330 500,270 530,262 C555,256 560,215 555,195 C550,175 560,160 590,162 C620,165 680,160 720,160 H737 V430 H0 Z"/>
    <ellipse cx="556" cy="261" rx="50" ry="18" fill="var(--fish)"/>
  </svg>

  <p class="brand-name">Korvel Reefworks</p>
  <p class="tagline">We sell <strong>live saltwater fish</strong> and <strong>live corals</strong></p>

  <p class="contact-line contact-line--phone">
    <svg class="contact-icon" viewBox="0 0 32 32" aria-hidden="true"><circle cx="16" cy="16" r="16" fill="var(--cyan)"/><path d="M11 8.5c1-.6 2-.4 2.5.6l1.3 2.6c.4.8.2 1.6-.5 2.1l-1 .8c.8 2 2.4 3.6 4.4 4.5l.8-1c.5-.7 1.4-.9 2.1-.5l2.6 1.3c1 .5 1.2 1.6.6 2.5l-.8 1.1c-.7 1-2 1.4-3.2 1-5-1.7-8.6-5.3-10.3-10.3-.4-1.2 0-2.5 1-3.2z" fill="var(--card-blue)"/></svg>
    (856) 319-7264
  </p>
  <p class="contact-line contact-line--address">
    <svg class="contact-icon" viewBox="0 0 32 32" aria-hidden="true"><circle cx="16" cy="16" r="16" fill="var(--cyan)"/><path d="M16 7a6.5 6.5 0 0 0-6.5 6.5C9.5 18.5 16 25 16 25s6.5-6.5 6.5-11.5A6.5 6.5 0 0 0 16 7zm0 9.2a2.7 2.7 0 1 1 0-5.4 2.7 2.7 0 0 1 0 5.4z" fill="var(--card-blue)"/></svg>
    7 Halden Ct, Sewell, NJ. 08080
  </p>
</section>

<section class="card card--square">
  <svg class="reef-scene" viewBox="0 0 735 428" role="img" aria-label="Photograph of a coral reef aquarium with rocks, pink and purple corals, and an orange cartoon fish">
    <defs>
      <linearGradient id="reef-tones-b" x1="0" y1="0" x2="1" y2="0.3">
        <stop offset="0" stop-color="#4b4a5c"/>
        <stop offset="0.4" stop-color="#7d6e86"/>
        <stop offset="0.7" stop-color="#8d6fa8"/>
        <stop offset="0.85" stop-color="#c86a72"/>
        <stop offset="1" stop-color="#9fae4c"/>
      </linearGradient>
    </defs>
    <path fill="url(#reef-tones-b)" stroke="var(--outline)" stroke-width="3" d="M0,428 V352 C20,340 40,352 55,345 C70,338 85,290 95,280 C110,268 120,290 118,310 C116,330 125,345 140,340 C155,335 170,330 185,330 C195,300 190,265 205,258 C225,250 235,275 225,290 C215,305 245,300 250,310 C255,320 265,300 275,290 C285,275 300,265 315,280 C325,295 320,330 335,345 C345,340 350,320 360,300 C370,285 385,290 385,310 C385,330 390,345 405,340 C415,330 430,285 445,270 C460,255 470,270 468,300 C466,330 470,345 480,345 C490,330 500,270 530,262 C555,256 560,215 555,195 C550,175 560,160 590,162 C620,165 680,160 720,160 H737 V430 H0 Z"/>
    <ellipse cx="556" cy="261" rx="50" ry="18" fill="var(--fish)"/>
  </svg>

  <p class="brand-name">Korvel Reefworks</p>
  <p class="tagline">We sell <strong>live saltwater fish</strong> and <strong>live corals</strong></p>

  <p class="contact-line contact-line--phone">
    <svg class="contact-icon" viewBox="0 0 32 32" aria-hidden="true"><circle cx="16" cy="16" r="16" fill="var(--cyan)"/><path d="M11 8.5c1-.6 2-.4 2.5.6l1.3 2.6c.4.8.2 1.6-.5 2.1l-1 .8c.8 2 2.4 3.6 4.4 4.5l.8-1c.5-.7 1.4-.9 2.1-.5l2.6 1.3c1 .5 1.2 1.6.6 2.5l-.8 1.1c-.7 1-2 1.4-3.2 1-5-1.7-8.6-5.3-10.3-10.3-.4-1.2 0-2.5 1-3.2z" fill="var(--card-blue)"/></svg>
    (856) 319-7264
  </p>
  <p class="contact-line contact-line--address">
    <svg class="contact-icon" viewBox="0 0 32 32" aria-hidden="true"><circle cx="16" cy="16" r="16" fill="var(--cyan)"/><path d="M16 7a6.5 6.5 0 0 0-6.5 6.5C9.5 18.5 16 25 16 25s6.5-6.5 6.5-11.5A6.5 6.5 0 0 0 16 7zm0 9.2a2.7 2.7 0 1 1 0-5.4 2.7 2.7 0 0 1 0 5.4z" fill="var(--card-blue)"/></svg>
    7 Halden Ct, Sewell, NJ. 08080
  </p>
</section>

</body>
</html>
```